We would like to design a logo, letter head, and business card.  

We have beauty colleges in the Kansas City Missouri USA area that have been around for 55 years.  We teach hair, skin and nail tech programs to students. Most of our students are female between the age of 18-30. 

Updates

• I appologize for failing to provide details on our addresses. We have 3 locations all with the same phone number.

Hall of Marquette 3140 NE County Rd 12 Blue Springs MO 64027

Hall of Marquette 4810 Pellham Kansas City MO 64125

Hall of Marquette 13460 Oak Hollow Blvd Grandview Mo 64138

Phone: (816) 555-0147

• Dale Marquette

President

3140 NE County Rd 12

Blue Springs MO 64027

(816) 555-0147

dale@trq-salonschool.com
Updates

Target Market(s)

18-30 Years Old

Industry/Entity Type

Business

Logo Text

Hall of Marquette Beauty College

Requirements
Must have
• Hall of Marquette Beauty College

```html
<!DOCTYPE html>
<html lang="en">
<head>
<meta charset="utf-8">
<title>Hall of Marquette Beauty College – Identity</title>
<link rel="stylesheet" href="https://fonts.googleapis.com/css2?family=Arimo:wght@400;700&display=swap">
<style>
  :root {
    --brand-red: #c8102e;
    --card-red: #c9002c;
    --ink: #1a1a1a;
    --sheet-edge: #e6a3b1;
    --card-edge: #b9b9b9;
    --paper: #ffffff;
  }
  * { box-sizing: border-box; margin: 0; padding: 0; }
  html, body {
    width: 830px; height: 1200px; overflow: hidden;
    background: var(--paper);
    font-family: "Arimo", Helvetica, Arial, sans-serif;
    color: var(--ink);
  }
  .canvas { position: relative; width: 830px; height: 1200px; }

  .wordmark {
    color: var(--brand-red);
    font-weight: 400;
    line-height: 1.15;
    display: flex; align-items: center; gap: 10px;
  }
  .wordmark .dot {
    width: 14px; height: 14px; border-radius: 50%;
    background: currentColor; flex: none;
  }

  /* Master logo */
  .master-logo { position: absolute; left: 29px; top: 112px; font-size: 34px; }
  .master-logo .dot { width: 22px; height: 22px; }

  /* Letterhead */
  .letterhead {
    position: absolute; left: 29px; top: 258px;
    width: 717px; height: 895px;
    border: 1px solid var(--sheet-edge);
    background: var(--paper);
  }
  .letterhead .wordmark {
    position: absolute; left: 0; right: 0; top: 46px;
    justify-content: center; font-size: 22px; text-align: center;
  }
  .letterhead-footer {
    position: absolute; left: 0; right: 0; top: 795px;
    text-align: center; font-size: 10.5px; line-height: 1.55;
  }
  .letterhead-footer .org { color: var(--brand-red); font-weight: 700; }

  /* Business card front */
  .card-front {
    position: absolute; left: 535px; top: 469px;
    width: 295px; height: 164px;
    background: var(--card-red);
  }
  .card-front .wordmark {
    position: absolute; right: 20px; top: 118px;
    color: var(--paper); font-size: 11px; gap: 6px;
  }
  .card-front .wordmark .dot { width: 8px; height: 8px; }

  /* Business card back */
  .card-back {
    position: absolute; left: 535px; top: 659px;
    width: 295px; height: 162px;
    border: 1px solid var(--card-edge);
    background: var(--paper);
    padding: 20px 0 0 84px;
    font-size: 8.5px; line-height: 1.45;
  }
  .card-back .name,
  .card-back .org { color: var(--brand-red); font-weight: 700; font-size: 9.5px; }
  .card-back .title { margin-bottom: 7px; }
  .card-back .contact { margin-bottom: 12px; }
</style>
</head>
<body>
<main class="canvas">

  <div class="wordmark master-logo">
    <span class="dot"></span>
    <span>Hall of Marquette<br>Beauty College</span>
  </div>

  <section class="letterhead" aria-label="Letterhead">
    <div class="wordmark">
      <span class="dot"></span>
      <span>Hall of Marquette<br>Beauty College</span>
    </div>
    <footer class="letterhead-footer">
      <p class="org">Hall of Marquette</p>
      <p>3140 NE County Rd 12 Blue Springs MO 64027</p>
      <p>4810 Pellham Kansas City MO 64125</p>
      <p>13460 Oak Hollow Blvd Grandview Mo 64138</p>
      <p>t. (816) 555-0147</p>
    </footer>
  </section>

  <section class="card-front" aria-label="Business card front">
    <div class="wordmark">
      <span class="dot"></span>
      <span>Hall of Marquette<br>Beauty College</span>
    </div>
  </section>

  <section class="card-back" aria-label="Business card back">
    <p class="name">Dale Marquette</p>
    <p class="title">President</p>
    <div class="contact">
      <p>3140 NE County Rd 12 Blue Springs MO 64027</p>
      <p>t. (816) 555-0147</p>
      <p>e. dale@trq-salonschool.com</p>
    </div>
    <p class="org">Hall of Marquette</p>
    <p>3140 NE County Rd 12 Blue Springs MO 64027</p>
    <p>4810 Pellham Kansas City MO 64125</p>
    <p>13460 Oak Hollow Blvd Grandview Mo 64138</p>
  </section>

</main>
</body>
</html>
```